Travel, Resort and Tourism Advisor

I am looking for a classy and slick website for a travel, resort and tourism website which will offer first hand advise to tourist and fun seekers on the best locations and remarkable places to relax and unwind. We are primary located in the United States but will offer services to people worldwide. My website will feature images and locations and analysis of the best resorts in the Industry. Designers can take an idea from http://wanderpinion.example It will include prices, safety tips, culture and how to make the best of your tourism. The website will compare different destinations and recommend places based on the user budget, culture, and ethnic nationality. I would want a colorful and attention seeking website. Have questions ask.
Industry/Entity Type
Tourism
Coding
Coded - Design and coding required
Number of Pages Required
1 page
Look and feel
Each slider illustrates characteristics of the customer's brand and the style your logo design should communicate.

```html
<!DOCTYPE html>
<html lang="en">
<head>
<meta charset="utf-8">
<title>Travel Guide</title>
<link href="https://fonts.googleapis.com/css2?family=Lato:ital,wght@0,400;0,700;0,900;1,700&display=swap" rel="stylesheet">
<style>
:root{
  --green:#5cb82e;
  --ink:#2b2b2b;
  --muted:#8a8a8a;
  --light:#f3f3f3;
  --footer:#f5f5f5;
  --bar:#ececec;
  --white:#ffffff;
  --card-foot:#3a3d42;
}
*{box-sizing:border-box;margin:0;padding:0}
html,body{width:1200px;height:2839px;overflow:hidden}
body{font-family:'Lato',Arial,sans-serif;color:var(--ink);background:var(--white);position:relative}
a{color:inherit;text-decoration:none}
.icon-defs{position:absolute;width:0;height:0}

/* hero */
.hero{position:relative;height:543px;background:linear-gradient(180deg,#3d4c5c 0%,#6d7a80 30%,#b59a62 55%,#5a4a33 80%,#2c2a25 100%);color:var(--white)}
.hero-photo{position:absolute;inset:0;background:radial-gradient(ellipse 300px 160px at 1010px 300px,rgba(255,220,140,.75),transparent),radial-gradient(ellipse 700px 260px at 200px 200px,rgba(60,70,40,.6),transparent)}
.topbar{position:absolute;left:0;right:0;top:0;height:42px;background:rgba(20,28,36,.55);border-bottom:1px solid rgba(255,255,255,.15)}
.topbar-links{position:absolute;left:74px;top:13px;display:flex;gap:28px;font-size:12px;font-weight:700}
.topbar-links span::before{content:"";display:inline-block;width:10px;height:9px;background:var(--white);border-radius:2px;margin-right:8px;vertical-align:-1px}
.topbar-tools{position:absolute;right:74px;top:0;display:flex;height:42px}
.topbar-tools .tool{width:44px;height:42px;display:flex;align-items:center;justify-content:center;border-left:1px solid rgba(255,255,255,.15)}
.topbar-tools .social{width:14px;height:14px;background:var(--white);border-radius:2px}
.topbar-tools .active{border-bottom:3px solid #2aa4e0}
.brand{position:absolute;left:74px;top:50px;font-size:38px;font-weight:700;letter-spacing:-.5px}
.nav{position:absolute;right:74px;top:66px;display:flex;gap:28px;font-size:13px;font-weight:700}
.nav .drop::after{content:"";display:inline-block;border:4px solid transparent;border-top-color:var(--white);margin-left:6px;vertical-align:-1px}
.hero-title{position:absolute;left:74px;top:312px;font-size:46px;font-weight:700}
.hero-sub{position:absolute;left:74px;top:374px;font-size:20px;color:rgba(255,255,255,.88)}
.section-label{font-size:16px;font-weight:900;text-transform:uppercase;display:flex;align-items:center;gap:16px}
.chip{background:var(--green);color:var(--white);font-size:11px;font-weight:700;text-transform:none;padding:5px 12px;border-radius:2px}
.chip::after{content:" ›"}
.hero .section-label{position:absolute;left:74px;top:458px}

/* featured */
.featured{background:var(--light);height:233px;position:relative}
.featured-grid{position:absolute;left:74px;top:-41px;display:flex;gap:34px}
.dest-card{width:238px;height:240px;background:var(--white);box-shadow:0 1px 3px rgba(0,0,0,.12)}
.dest-photo{height:180px}
.dest-name{font-size:14px;font-weight:700;padding:13px 14px 2px}
.dest-region{font-size:10px;color:var(--muted);padding:0 14px}
.dest-region::before{content:"";display:inline-block;width:6px;height:8px;background:var(--muted);border-radius:50% 50% 50% 50%/60% 60% 40% 40%;margin-right:6px}

/* advisor strip */
.advisor{height:248px;position:relative;background:var(--white)}
.advisor-name{position:absolute;left:104px;top:100px;font-size:44px;font-weight:700;color:var(--ink);display:flex;align-items:center;gap:14px}
.advisor-name .dot{width:22px;height:22px;border-radius:50%;background:var(--green)}
.advisor-tag{position:absolute;left:524px;top:76px;font-size:22px;font-weight:700}
.advisor-tag em{color:var(--green)}
.search{position:absolute;left:452px;top:127px;width:655px;height:45px;border:2px solid #9a9a9a;border-radius:23px;display:flex;align-items:center;padding:0 18px;font-size:18px;color:#9a9a9a;justify-content:space-between}

/* categories */
.categories{background:var(--light);height:594px;position:relative}
.cat-grid{position:absolute;left:74px;top:55px;display:flex;gap:34px}
.cat-card{width:327px;height:471px;background:var(--white);box-shadow:0 1px 3px rgba(0,0,0,.1);position:relative}
.cat-head{height:108px;padding:16px 14px}
.cat-title{font-size:16px;font-weight:900;text-transform:uppercase}
.cat-text{font-size:12px;color:var(--muted);margin-top:10px;line-height:1.55}
.cat-row{height:64px;position:relative;color:var(--white)}
.cat-row.lead{height:200px}
.cat-place{position:absolute;left:54px;bottom:12px}
.cat-place b{display:block;font-size:14px}
.cat-place span{font-size:10px;opacity:.75}
.cat-row svg{position:absolute;left:16px;bottom:18px}
.cat-more{position:absolute;right:14px;bottom:9px;font-size:11px;color:var(--muted);font-weight:700}
.cat-more::after{content:" ➔";color:#555}

/* spotlight */
.spotlight{height:527px;position:relative;background:linear-gradient(180deg,#8fa6b8 0%,#c9a9a0 28%,#7d95a6 44%,#3f6a86 62%,#24506b 82%,#1e4660 100%);color:var(--white)}
.spotlight-title{position:absolute;left:617px;top:145px;font-size:44px;font-weight:700}
.spotlight-text{position:absolute;left:617px;top:225px;width:505px;font-size:20px;line-height:1.5}
.btn{position:absolute;left:617px;top:343px;background:var(--green);font-size:12px;font-weight:700;padding:9px 20px;border-radius:2px}
.btn::after{content:"  ›"}

/* news */
.news{height:556px;position:relative;background:var(--white)}
.news .section-label{position:absolute;left:74px;top:74px}
.news-grid{position:absolute;left:74px;top:117px;display:flex;gap:34px}
.news-card{width:238px;height:358px;position:relative;color:var(--white)}
.news-photo{height:316px;position:relative}
.news-title{position:absolute;left:14px;bottom:14px;font-size:21px;font-weight:700;line-height:1.15}
.news-meta{height:42px;background:var(--card-foot);display:flex;justify-content:space-between;align-items:center;padding:0 14px;font-size:10px}
.news-meta span::before{content:"";display:inline-block;width:8px;height:8px;border-radius:50%;background:#aaa;margin-right:6px}

/* footer */
.footer{height:88px;background:var(--footer);position:relative}
.footer-links{position:absolute;left:74px;top:58px;display:flex;gap:16px;font-size:10px;color:#555}
.footer-brand{position:absolute;right:74px;top:20px;font-size:38px;font-weight:700;color:#333}
.legal{height:50px;background:var(--bar);font-size:10px;color:#888;padding:20px 74px}
</style>
</head>
<body>
<svg class="icon-defs" aria-hidden="true"><symbol id="pin" viewBox="0 0 12 16"><path d="M6 0a6 6 0 0 1 6 6c0 4-6 10-6 10S0 10 0 6a6 6 0 0 1 6-6z" fill="#fff"/><circle cx="6" cy="6" r="2.2" fill="#333"/></symbol></svg>

<header class="hero">
  <div class="hero-photo" role="img" aria-label="Winding coastal road over green hills at sunset with a runner"></div>
  <div class="topbar">
    <div class="topbar-links"><span>Contact Us</span><span>Join the Explorers!</span><span>Sign in</span></div>
    <div class="topbar-tools">
      <div class="tool"><svg width="16" height="16" viewBox="0 0 16 16"><circle cx="6.5" cy="6.5" r="5" fill="none" stroke="#fff" stroke-width="2"/><path d="M10 10l5 5" stroke="#fff" stroke-width="2.4"/></svg></div>
      <div class="tool active"><i class="social"></i></div>
      <div class="tool"><i class="social"></i></div>
      <div class="tool"><i class="social"></i></div>
      <div class="tool"><i class="social"></i></div>
    </div>
  </div>
  <div class="brand">Travel Guide</div>
  <nav class="nav"><a class="drop">Destinations</a><a class="drop">Explore</a><a>News &amp; Articles</a><a>About</a></nav>
  <h1 class="hero-title">Discover your journey</h1>
  <p class="hero-sub">We offer first hand advise to tourist and fun seekers on the best locations and remarkable places to relax and unwind.</p>
  <div class="section-label">Featured Destinations <span class="chip">Find More</span></div>
</header>

<section class="featured">
  <div class="featured-grid">
    <article class="dest-card"><div class="dest-photo" role="img" aria-label="Harbour with opera house at dusk" style="background:linear-gradient(180deg,#5a6fa0,#c58a7a 60%,#2c3350)"></div><div class="dest-name">Sydney, Australia</div><div class="dest-region">Oceania</div></article>
    <article class="dest-card"><div class="dest-photo" role="img" aria-label="Glowing orange slot canyon walls" style="background:linear-gradient(135deg,#5a1e10,#d2672a 50%,#7a2a14)"></div><div class="dest-name">Yellowstone, USA</div><div class="dest-region">North America</div></article>
    <article class="dest-card"><div class="dest-photo" role="img" aria-label="Lakeside town with snowy mountains" style="background:linear-gradient(180deg,#6e8fb8,#d5d8de 35%,#3b4a5e 60%,#2a3240)"></div><div class="dest-name">Queenstown, New Zealand</div><div class="dest-region">Oceania</div></article>
    <article class="dest-card"><div class="dest-photo" role="img" aria-label="Red suspension bridge over the bay" style="background:linear-gradient(180deg,#8fbbe0,#c9dcea 55%,#b0452e 75%,#3f5f7a)"></div><div class="dest-name">San Francisco, USA</div><div class="dest-region">North America</div></article>
  </div>
</section>

<section class="advisor">
  <div class="advisor-name"><span class="dot"></span>wanderpinion</div>
  <p class="advisor-tag">Be more than just another traveler when you <em>Go Travel</em></p>
  <div class="search">Find Your Next Destination... <svg width="22" height="22" viewBox="0 0 16 16"><circle cx="6.5" cy="6.5" r="5" fill="none" stroke="#8a8a8a" stroke-width="2"/><path d="M10 10l5 5" stroke="#8a8a8a" stroke-width="2.4"/></svg></div>
</section>

<section class="categories">
  <div class="cat-grid">
    <article class="cat-card">
      <div class="cat-head"><h3 class="cat-title">Adventure Seekers</h3><p class="cat-text">With endless hiking trails, these destinations will satisfy the wildest explorers!</p></div>
      <div class="cat-row lead" role="img" aria-label="City rooftops at golden hour" style="background:linear-gradient(180deg,#c9a070,#8a6a50 55%,#4a3a32)"><svg width="14" height="19"><use href="#pin"/></svg><div class="cat-place"><b>Buenos Aires, Argentina</b><span>South America</span></div></div>
      <div class="cat-row" role="img" aria-label="Mountain lake town" style="background:linear-gradient(90deg,#3a4a60,#2a3442)"><svg width="14" height="19"><use href="#pin"/></svg><div class="cat-place"><b>Queenstown, New Zealand</b><span>Oceania</span></div></div>
      <div class="cat-row" role="img" aria-label="Snowy alpine peak" style="background:linear-gradient(90deg,#6d7384,#a5aab5)"><svg width="14" height="19"><use href="#pin"/></svg><div class="cat-place"><b>Zermatt, Switzerland</b><span>Europe</span></div></div>
      <a class="cat-more">Find More</a>
    </article>
    <article class="cat-card">
      <div class="cat-head"><h3 class="cat-title">Beach Lovers</h3><p class="cat-text">Head for a swim and relax on the warm, golden sand. Life's a beach!</p></div>
      <div class="cat-row lead" role="img" aria-label="Bay with hotels and blue sea" style="background:linear-gradient(180deg,#9fb6c8,#6a9ab0 45%,#1f5a72)"><svg width="14" height="19"><use href="#pin"/></svg><div class="cat-place"><b>Acapulco, Mexico</b><span>North America</span></div></div>
      <div class="cat-row" role="img" aria-label="Turquoise water and white sand" style="background:linear-gradient(90deg,#2f8aa0,#4aa2b0)"><svg width="14" height="19"><use href="#pin"/></svg><div class="cat-place"><b>Whitehaven Beach, Australia</b><span>Oceania</span></div></div>
      <div class="cat-row" role="img" aria-label="Golden coastal cliffs" style="background:linear-gradient(90deg,#6a4a30,#a07a50)"><svg width="14" height="19"><use href="#pin"/></svg><div class="cat-place"><b>Algarve, Portugal</b><span>Europe</span></div></div>
      <a class="cat-more">Find More</a>
    </article>
    <article class="cat-card">
      <div class="cat-head"><h3 class="cat-title">Crowd Escapers</h3><p class="cat-text">Step away from the crowd, explore places where you'll feel no one has ever been before.</p></div>
      <div class="cat-row lead" role="img" aria-label="Sea turtle swimming in deep blue water" style="background:linear-gradient(180deg,#0c2232,#1a3e52 60%,#1f4e66)"><svg width="14" height="19"><use href="#pin"/></svg><div class="cat-place"><b>Galapagos Islands, Ecuador</b><span>South America</span></div></div>
      <div class="cat-row" role="img" aria-label="Colourful canyon rock" style="background:linear-gradient(90deg,#6a3a22,#8a5030)"><svg width="14" height="19"><use href="#pin"/></svg><div class="cat-place"><b>Yellowstone, USA</b><span>North America</span></div></div>
      <div class="cat-row" role="img" aria-label="Waterfalls in green jungle" style="background:linear-gradient(90deg,#3e5a40,#7a8c70)"><svg width="14" height="19"><use href="#pin"/></svg><div class="cat-place"><b>Foz do Iguacu, Brasil</b><span>South America</span></div></div>
      <a class="cat-more">Find More</a>
    </article>
  </div>
</section>

<section class="spotlight" role="img" aria-label="White limestone cliff above a calm sea at sunset with visitors">
  <h2 class="spotlight-title">Scala dei Turchi, Italy</h2>
  <p class="spotlight-text">Near southern Sicily, the Scala has become an attraction thanks to its unusual white color. Formed by a sedimentary rock with a distinct white color…..</p>
  <a class="btn">Read More</a>
</section>

<section class="news">
  <div class="section-label">News Articles &amp; Blogs <span class="chip">Find More</span></div>
  <div class="news-grid">
    <article class="news-card"><div class="news-photo" role="img" aria-label="People walking across a stone bridge" style="background:linear-gradient(180deg,#d6d2c8,#7a6e62 55%,#2e2a28)"><h3 class="news-title">Living the Travel<br>Lifestyle</h3></div><div class="news-meta"><span>Olivia</span>May 11, 2015</div></article>
    <article class="news-card"><div class="news-photo" role="img" aria-label="Traveller reading a map on a train" style="background:linear-gradient(180deg,#4e6a3a,#9a4030 55%,#2e2420)"><h3 class="news-title">Choosing Your Next<br>Vacation Destination</h3></div><div class="news-meta"><span>Jack</span>May 6, 2015</div></article>
    <article class="news-card"><div class="news-photo" role="img" aria-label="Railway platform with sunlight at the end" style="background:linear-gradient(180deg,#3a3a3a,#c98a40 55%,#2a2622)"><h3 class="news-title">Unusual Places to<br>Consider Visiting</h3></div><div class="news-meta"><span>Emily</span>April 20, 2015</div></article>
    <article class="news-card"><div class="news-photo" role="img" aria-label="City street with a red double-decker bus" style="background:linear-gradient(180deg,#d9c9b0,#8a7056 55%,#3a2a22)"><h3 class="news-title">8 Useful Tools for<br>Planning a Great Trip</h3></div><div class="news-meta"><span>Mason</span>April 11, 2015</div></article>
  </div>
</section>

<footer>
  <div class="footer">
    <nav class="footer-links"><a>About Us</a><a>Sign in</a><a>Be an Explorer!</a><a>Destinations</a><a>Blog</a><a>Contact us</a></nav>
    <div class="footer-brand">Travel Guide</div>
  </div>
  <div class="legal">© 2016 Travel Guide. Terms of Use and Privacy Policy.</div>
</footer>
</body>
</html>
```